Harborlight Crest Development, a residential real estate development company, needs a logo / busine

logo & business card design is needed for a new company based in Dallas, TX.
Name: Harborlight Crest Development, LLC (HLC Development)
We are a residential real estate development company seeking to change neighborhoods one house at a time. Providing individuals and families homes in a neighborhood community where they want to live rather the mcmansion developments we've seen developed the past couple of decades.
The final design should be simplistic, professional and convey a unique, but sophisticated image.

info for the business card:

Renata J. Pollard
President

address: P.O. Box 30716, Dallas, TX 75241
phone: 214.555.0173
email: rpollard@hlc-buildhomes.example

Requirements
Should not have
• No black in the design (i.e stripes, waves etc. ok for the font)

```html
<!DOCTYPE html>
<html lang="en">
<head>
<meta charset="UTF-8">
<title>HLC Development — Business Card</title>
<link href="https://fonts.googleapis.com/css2?family=Montserrat:ital,wght@0,400;0,500;0,700;1,400&display=swap" rel="stylesheet">
<style>
  :root {
    --charcoal: #414042;
    --coral: #f26a44;
    --stone: #c7c8ca;
    --slate: #6d6e71;
    --paper: #ffffff;
  }
  * { margin: 0; padding: 0; box-sizing: border-box; }
  html, body { width: 1200px; height: 1000px; overflow: hidden; background: var(--paper); }
  body { position: relative; font-family: "Montserrat", Arial, sans-serif; }

  .card {
    position: absolute;
    left: 330px;
    width: 527px;
    height: 322px;
    background: var(--charcoal);
    overflow: hidden;
  }
  .card--front { top: 128px; }
  .card--back { top: 468px; }
  .card .accent { position: absolute; left: 0; top: 0; }

  .wordmark {
    position: absolute;
    display: flex;
    align-items: center;
    white-space: nowrap;
    font-weight: 500;
    color: var(--paper);
  }
  .wordmark .mark-square { background: var(--stone); flex: none; }

  .card--front .wordmark { left: 70px; top: 69px; font-size: 33px; }
  .card--front .mark-square { width: 37px; height: 37px; margin-right: 15px; }

  .card--back .wordmark { left: 222px; top: 262px; font-size: 21px; }
  .card--back .mark-square { width: 24px; height: 24px; margin-right: 10px; }

  .contact {
    position: absolute;
    left: 66px;
    top: 38px;
    color: var(--paper);
  }
  .contact .pointer { position: absolute; left: -22px; top: 1px; }
  .contact .name { font-weight: 700; font-size: 17px; letter-spacing: 0.3px; line-height: 22px; }
  .contact .title { font-style: italic; font-size: 13px; line-height: 18px; opacity: 0.9; }
  .contact .address { font-size: 15.5px; line-height: 20px; margin-top: 7px; }
  .contact .phone { font-weight: 700; font-size: 16px; letter-spacing: 0.5px; line-height: 20px; margin-top: 9px; }
  .contact .email { font-size: 12.5px; line-height: 17px; }

  .brand-signature {
    position: absolute;
    left: 565px;
    top: 893px;
    display: flex;
    align-items: center;
    white-space: nowrap;
    font-size: 50px;
    font-weight: 500;
    color: var(--charcoal);
  }
  .brand-signature .mark-square { width: 51px; height: 51px; margin-right: 21px; background: var(--slate); }
</style>
</head>
<body>

  <section class="card card--front">
    <svg class="accent" width="527" height="322" viewBox="0 0 527 322" aria-hidden="true">
      <polygon points="0,185 527,322 0,322" fill="var(--coral)"/>
    </svg>
    <div class="wordmark"><span class="mark-square"></span>HLC Development</div>
  </section>

  <section class="card card--back">
    <svg class="accent" width="527" height="322" viewBox="0 0 527 322" aria-hidden="true">
      <polygon points="527,0 445,81 527,163" fill="var(--coral)"/>
    </svg>
    <div class="contact">
      <svg class="pointer" width="12" height="22" viewBox="0 0 12 22" aria-hidden="true">
        <polygon points="0,0 12,11 0,22" fill="var(--coral)"/>
      </svg>
      <p class="name">RENATA J. POLLARD</p>
      <p class="title">President</p>
      <p class="address">P.O. Box 30716,<br>Dallas, TX 75241</p>
      <p class="phone">xxx.xxx.xxxx</p>
      <p class="email">rpollard@hlc-buildhomes.example</p>
    </div>
    <div class="wordmark"><span class="mark-square"></span>HLC Development</div>
  </section>

  <div class="brand-signature"><span class="mark-square"></span>HLC Development</div>

</body>
</html>
```